Business card for a "family office" company

Please provide professional looking business card designs, incorporating the attached logo and below details. Harrowmere Holdings Pty Ltd is a family office / financial investment company. We are looking for a modern, professional and contemporary card design.

Industry/Entity Type

Finance

Contact Information for Business Card

Name: Dean Mollick
Title: Director
Company: Harrowmere Holdings Pty Ltd
Email: harrowdean@quillnet.example
Mobile: 0462 735 418
Address: 4/312 Barnaby Parade, Fernhollow WA 6094, Australia

Requirements
Must have
• All details above and the logo. logo only on back side. incorporate colours of logo
Nice to have
• up to you
Should not have
• ?

```html
<!DOCTYPE html>
<html lang="en">
<head>
<meta charset="utf-8">
<title>Harrowmere Holdings – Business Card</title>
<link rel="stylesheet" href="https://fonts.googleapis.com/css2?family=PT+Sans:wght@400;700&display=swap">
<style>
  :root {
    --stage: #000000;
    --card-light: #f3f3f3;
    --navy: #1f1d5c;
    --navy-back: #22205f;
    --ink: #222222;
    --white: #ffffff;
  }
  * { margin: 0; padding: 0; box-sizing: border-box; }
  html, body {
    width: 1200px; height: 900px; overflow: hidden;
    background: var(--stage);
    font-family: "PT Sans", "Helvetica Neue", Arial, sans-serif;
  }
  .canvas { position: relative; width: 1200px; height: 900px; }

  .card { position: absolute; top: 200px; width: 310px; height: 502px; }
  .card-front {
    left: 265px; background: var(--card-light);
    border-radius: 52px 0 52px 0;
  }
  .card-back {
    left: 641px; width: 309px; background: var(--navy-back);
    border-radius: 0 58px 0 58px;
  }

  .brand-mark {
    position: absolute; left: 50%; transform: translateX(-50%);
    width: 48px; height: 48px; background: var(--navy);
  }
  .card-front .brand-mark { top: 66px; }
  .brand-name {
    position: absolute; left: 0; right: 0; text-align: center;
    font-weight: 400; color: var(--navy); line-height: 1;
  }
  .brand-name .primary { display: block; font-size: 33px; letter-spacing: 1.5px; }
  .brand-name .secondary { display: block; font-size: 14px; letter-spacing: 6px; margin-top: 6px; }
  .card-front .brand-name { top: 143px; }
  .card-back .brand-name { top: 409px; color: var(--white); }

  .contact { position: absolute; left: 20px; top: 295px; color: var(--ink); }
  .person-name { font-size: 18px; font-weight: 700; color: var(--navy); line-height: 1.1; }
  .person-title { font-size: 13px; line-height: 1.3; }
  .company-name { margin-top: 26px; font-size: 15px; font-weight: 700; color: var(--navy); line-height: 1.3; }
  .address { font-size: 13.5px; line-height: 21px; margin-top: 1px; }
  .contact-lines { margin-top: 13px; font-size: 13.5px; line-height: 21px; }
  .contact-line { display: flex; align-items: center; gap: 5px; }
  .contact-line svg { width: 10px; height: 10px; fill: var(--navy); flex: none; }
</style>
</head>
<body>
<main class="canvas">
  <section class="card card-front" aria-label="Business card front">
    <div class="brand-mark"></div>
    <div class="brand-name">
      <span class="primary">HARROWMERE</span>
      <span class="secondary">HOLDINGS</span>
    </div>
    <div class="contact">
      <p class="person-name">Dean Mollick</p>
      <p class="person-title">Director</p>
      <p class="company-name">Harrowmere Holdings Pty Ltd</p>
      <p class="address">4/312 Barnaby Parade,<br>Fernhollow WA 6094, Australia</p>
      <div class="contact-lines">
        <p class="contact-line">
          <svg viewBox="0 0 10 10" aria-hidden="true"><path d="M2.2 0.5 L3.6 2.6 L2.8 3.6 C3.4 5 4.9 6.5 6.4 7.2 L7.4 6.4 L9.5 7.8 L8.6 9.4 C4.5 9.2 0.8 5.5 0.6 1.4 Z"/></svg>
          0462 735 418
        </p>
        <p class="contact-line">
          <svg viewBox="0 0 10 10" aria-hidden="true"><path d="M0.5 2 H9.5 V8.5 H0.5 Z M0.5 2 L5 5.6 L9.5 2" fill="var(--navy)" stroke="var(--card-light)" stroke-width="0.8"/></svg>
          harrowdean@quillnet.example
        </p>
      </div>
    </div>
  </section>

  <section class="card card-back" aria-label="Business card back">
    <div class="brand-name">
      <span class="primary">HARROWMERE</span>
      <span class="secondary">HOLDINGS</span>
    </div>
  </section>
</main>
</body>
</html>
```